Window and GutterCleaning Flyer A5 size double sided.

We need a double sided A5 flyer. Side 1, is for window cleaning, side 2 is for gutter cleaning. Licensed by Borough of Halvern Council.
Phone number 0800 315 4720.
Business address 7 Tarnlow Brae, North Pellin Edinburgh EH14 3RW.
www.clearpane-vista-services.com
We use a LoftPro Gutter inspection Cam to view your gutters first to see if they need doing.
Window cleaning ; Professional window cleaning services, what we offer, water fed pole window cleaning able to reach windows up to 60 feet.
Conservatory cleaning.
Conservatory roof cleaning.
Fascias & Soffits cleaning.
Excellent Customer Service.
Target Market(s)
domestic houses
Industry/Entity Type
window cleaning
Look and feel
Each slider illustrates characteristics of the customer's brand and the style your logo design should communicate.

```html
<!DOCTYPE html>
<html lang="en">
<head>
<meta charset="utf-8">
<title>ClearPane Vista Services – Flyers</title>
<link href="https://fonts.googleapis.com/css2?family=Bebas+Neue&family=Roboto:wght@400;500;700;900&display=swap" rel="stylesheet">
<style>
  :root {
    --navy: #25245e;
    --sky: #3fa3dc;
    --sky-light: #66c7f3;
    --pale: #9fc8ee;
    --page: #ebecee;
    --white: #ffffff;
  }
  * { margin: 0; padding: 0; box-sizing: border-box; }
  html, body { width: 1200px; height: 1200px; overflow: hidden; }
  body { background: var(--page); position: relative; font-family: "Roboto", sans-serif; }

  .flyer {
    position: absolute; top: 264px; width: 480px; height: 672px;
    background: var(--white); overflow: hidden;
    box-shadow: 0 6px 14px rgba(0,0,0,0.35);
  }
  .flyer--window { left: 109px; }
  .flyer--gutter { left: 611px; }

  .hero { position: absolute; left: 0; top: 0; width: 480px; height: 300px; display: block; }

  .brand {
    position: absolute; left: 35px; top: 160px; width: 127px;
    background: var(--pale); padding: 5px 4px 4px;
    font-family: "Bebas Neue", sans-serif; color: var(--navy);
    font-size: 21px; line-height: 0.95; text-align: center; letter-spacing: 0.5px;
  }

  .badge { position: absolute; left: 317px; top: 194px; width: 102px; height: 102px; }
  .badge text { font-family: "Bebas Neue", sans-serif; text-anchor: middle; }

  .headline { position: absolute; left: 35px; top: 324px; font-family: "Bebas Neue", sans-serif; color: var(--navy); }
  .headline__lead { font-size: 25px; line-height: 1; letter-spacing: 0.2px; }
  .headline__main { font-size: 62px; line-height: 0.86; color: var(--sky); letter-spacing: 0.5px; }
  .headline__tail { font-size: 25px; line-height: 1; }

  .services { position: absolute; left: 264px; top: 318px; }
  .flyer--gutter .services { left: 272px; top: 324px; }
  .section-title { font-family: "Bebas Neue", sans-serif; color: var(--navy); font-size: 30px; line-height: 1; letter-spacing: 0.3px; }
  .services ul { list-style: none; margin-top: 6px; }
  .services li { color: var(--sky); font-size: 12.3px; line-height: 19px; padding-left: 15px; position: relative; }
  .services li::before {
    content: ""; position: absolute; left: 0; top: 7px; width: 6px; height: 6px;
    border-radius: 50%; background: var(--sky);
  }

  .offer { position: absolute; left: 35px; top: 438px; }
  .flyer--gutter .offer { top: 446px; }
  .offer .section-title { font-size: 25px; }
  .offer p { margin-top: 4px; color: var(--sky); font-size: 11.6px; line-height: 17.5px; letter-spacing: 0.4px; text-transform: uppercase; font-weight: 500; }

  .contact {
    position: absolute; left: 0; top: 562px; width: 480px; height: 110px;
    background: linear-gradient(90deg, #46a8df 0%, var(--sky-light) 55%, #46a8df 100%);
  }
  .cta {
    position: absolute; left: 142px; top: 544px; width: 197px; height: 36px;
    background: var(--navy); border-radius: 7px; color: var(--white);
    font-family: "Bebas Neue", sans-serif; font-size: 29px; line-height: 38px; text-align: center;
  }
  .phone {
    position: absolute; left: 0; top: 582px; width: 480px; text-align: center;
    color: var(--white); font-weight: 700; font-size: 39px; letter-spacing: 0.5px;
  }
  .details {
    position: absolute; left: 0; top: 627px; width: 480px; display: flex; justify-content: center; gap: 10px;
    color: var(--white); font-size: 9.2px; white-space: nowrap;
  }
  .details span { display: inline-flex; align-items: center; gap: 3px; }
  .details svg { width: 8px; height: 8px; }
</style>
</head>
<body>

<!-- Side 1: window cleaning -->
<article class="flyer flyer--window">
  <svg class="hero" viewBox="0 0 480 300" aria-hidden="false">
    <defs>
      <linearGradient id="windowPhoto" x1="0" y1="0" x2="1" y2="0">
        <stop offset="0" stop-color="#c9cfd6"/>
        <stop offset="0.45" stop-color="#9a5a45"/>
        <stop offset="1" stop-color="#6f8fc0"/>
      </linearGradient>
    </defs>
    <rect width="480" height="300" fill="url(#windowPhoto)" role="img" aria-label="Photos of water fed pole window cleaning on a brick house"/>
    <path d="M0,262 C150,285 330,255 480,175 L480,196 C330,278 150,306 0,292 Z" fill="#4bb2e6"/>
    <path d="M0,285 C150,302 330,272 480,190 L480,300 L0,300 Z" fill="#ffffff"/>
  </svg>

  <div class="brand">ClearPane<br>Vista</div>

  <svg class="badge" viewBox="0 0 102 102">
    <circle cx="51" cy="51" r="48" fill="#fff" stroke="#25245e" stroke-width="5"/>
    <circle cx="51" cy="51" r="40" fill="none" stroke="#25245e" stroke-width="1"/>
    <text x="51" y="39" font-size="20" fill="#25245e">100%</text>
    <text x="51" y="53" font-size="14" fill="#9fc8ee">CUSTOMER</text>
    <text x="51" y="64" font-size="11" fill="#25245e">SATISFACTION</text>
    <text x="51" y="75" font-size="12" fill="#9fc8ee" letter-spacing="1">GUARANTEE</text>
  </svg>

  <div class="headline">
    <div class="headline__lead">Professional Window</div>
    <div class="headline__main">Cleaning</div>
    <div class="headline__tail">Services</div>
  </div>

  <section class="services">
    <h2 class="section-title">Our Services!</h2>
    <ul>
      <li>Conservatory cleaning.</li>
      <li>Conservatory roof cleaning.</li>
      <li>Fascias &amp; Soffits cleaning.</li>
      <li>Excellent Customer Service.</li>
    </ul>
  </section>

  <section class="offer">
    <h2 class="section-title">What We Offer!</h2>
    <p>Water fed pole window cleaning<br>able to reach windows up to 60 feet.</p>
  </section>

  <div class="contact"></div>
  <div class="cta">Call Us Today</div>
  <div class="phone">0800 315 4720</div>
  <div class="details">
    <span><svg viewBox="0 0 10 10"><circle cx="5" cy="5" r="4.2" fill="none" stroke="#fff" stroke-width="1"/><path d="M1 5h8M5 1v8" stroke="#fff" stroke-width="0.8"/></svg>www.clearpane-vista-services.com</span>
    <span><svg viewBox="0 0 10 10"><path d="M5 9.5 C2 6 2 4.5 2 3.8 a3 3 0 0 1 6 0 C8 4.5 8 6 5 9.5Z" fill="#fff"/><circle cx="5" cy="3.8" r="1.1" fill="#4bb2e6"/></svg>7 Tarnlow Brae, North Pellin Edinburgh EH14 3RW</span>
  </div>
</article>

<!-- Side 2: gutter cleaning -->
<article class="flyer flyer--gutter">
  <svg class="hero" viewBox="0 0 480 300">
    <defs>
      <linearGradient id="gutterPhoto" x1="0" y1="0" x2="1" y2="0.4">
        <stop offset="0" stop-color="#a9a7a2"/>
        <stop offset="0.5" stop-color="#7f8a6a"/>
        <stop offset="0.75" stop-color="#3147a8"/>
        <stop offset="1" stop-color="#b7bcc8"/>
      </linearGradient>
    </defs>
    <rect width="480" height="300" fill="url(#gutterPhoto)" role="img" aria-label="Photo of a gutter being cleared with a vacuum hose"/>
    <path d="M0,262 C150,285 330,255 480,175 L480,196 C330,278 150,306 0,292 Z" fill="#4bb2e6"/>
    <path d="M0,285 C150,302 330,272 480,190 L480,300 L0,300 Z" fill="#ffffff"/>
  </svg>

  <div class="brand">ClearPane<br>Vista</div>

  <svg class="badge" viewBox="0 0 102 102">
    <circle cx="51" cy="51" r="48" fill="#fff" stroke="#25245e" stroke-width="5"/>
    <circle cx="51" cy="51" r="40" fill="none" stroke="#25245e" stroke-width="1"/>
    <text x="51" y="39" font-size="20" fill="#25245e">100%</text>
    <text x="51" y="53" font-size="14" fill="#9fc8ee">CUSTOMER</text>
    <text x="51" y="64" font-size="11" fill="#25245e">SATISFACTION</text>
    <text x="51" y="75" font-size="12" fill="#9fc8ee" letter-spacing="1">GUARANTEE</text>
  </svg>

  <div class="headline">
    <div class="headline__lead">Professional Gutter</div>
    <div class="headline__main">Cleaning</div>
    <div class="headline__tail">Services</div>
  </div>

  <section class="services">
    <h2 class="section-title">Our Services!</h2>
    <ul>
      <li>Conservatory cleaning.</li>
      <li>Conservatory roof cleaning.</li>
      <li>Fascias &amp; Soffits cleaning.</li>
      <li>Excellent Customer Service.</li>
    </ul>
  </section>

  <section class="offer">
    <h2 class="section-title">What We Offer!</h2>
    <p>We use a LoftPro gutter inspection<br>cam to view your gutters first to see if they need doing.</p>
  </section>

  <div class="contact"></div>
  <div class="cta">Call Us Today</div>
  <div class="phone">0800 315 4720</div>
  <div class="details">
    <span><svg viewBox="0 0 10 10"><circle cx="5" cy="5" r="4.2" fill="none" stroke="#fff" stroke-width="1"/><path d="M1 5h8M5 1v8" stroke="#fff" stroke-width="0.8"/></svg>www.clearpane-vista-services.com</span>
    <span><svg viewBox="0 0 10 10"><path d="M5 9.5 C2 6 2 4.5 2 3.8 a3 3 0 0 1 6 0 C8 4.5 8 6 5 9.5Z" fill="#fff"/><circle cx="5" cy="3.8" r="1.1" fill="#4bb2e6"/></svg>7 Tarnlow Brae, North Pellin Edinburgh EH14 3RW</span>
  </div>
</article>

</body>
</html>
```